Brindle Capital and Investments

Create a simple business card design using the logos attached. Make it similar but not exact to the reference photo. Brand guidelines are also included.

```html
<!DOCTYPE html>
<html lang="en">
<head>
<meta charset="utf-8">
<title>Brindle Capital – Business Card</title>
<link rel="stylesheet" href="https://fonts.googleapis.com/css2?family=Noto+Serif:ital,wght@0,700;1,400&family=Poppins:wght@400;600&display=swap">
<style>
  :root {
    --navy: #0a0f3d;
    --rust: #8a4414;
    --ink: #3c3c3c;
    --paper: #fafafa;
    --backdrop: #e6e7eb;
    --white: #ffffff;
  }
  * { margin: 0; padding: 0; box-sizing: border-box; }
  html, body {
    width: 1200px; height: 800px; overflow: hidden;
    background: var(--backdrop);
    font-family: "Poppins", sans-serif;
  }
  .canvas {
    position: relative; width: 1200px; height: 800px;
    display: flex; align-items: center; justify-content: center; gap: 60px;
  }
  .card {
    position: relative; width: 525px; height: 300px;
    box-shadow: 0 6px 20px rgba(10, 15, 61, 0.18);
  }
  .card--front { background: var(--paper); }
  .card--back { background: var(--navy); display: flex; align-items: center; justify-content: center; }

  .wordmark {
    display: flex; align-items: center; gap: 10px;
    font-family: "Poppins", sans-serif; font-weight: 600;
    font-size: 22px; letter-spacing: 0.06em; text-transform: uppercase;
    line-height: 1.1;
  }
  .wordmark__dot { width: 12px; height: 12px; border-radius: 50%; background: var(--rust); flex: none; }
  .card--front .wordmark {
    position: absolute; left: 32px; top: 50%; transform: translateY(-50%);
    color: var(--navy); width: 190px;
  }
  .card--back .wordmark { color: var(--white); font-size: 34px; }

  .details { position: absolute; left: 245px; top: 38px; right: 24px; }
  .details__name {
    font-family: "Noto Serif", serif; font-weight: 700;
    font-size: 25px; color: var(--navy); letter-spacing: 0.02em; line-height: 1.1;
  }
  .details__role { font-size: 15px; color: var(--rust); margin-top: 2px; }
  .details__company { font-size: 13px; color: var(--navy); margin-top: 16px; }
  .details__address { font-size: 13px; color: var(--ink); line-height: 1.45; }
  .contact { margin-top: 14px; font-size: 13px; color: var(--ink); line-height: 1.45; }
  .contact__label {
    font-family: "Noto Serif", serif; font-style: italic; font-weight: 400;
    color: var(--rust); font-size: 14px; margin-right: 4px;
  }
</style>
</head>
<body>
  <main class="canvas">
    <section class="card card--front" aria-label="Business card front">
      <div class="wordmark"><span class="wordmark__dot"></span><span>Brindle Capital</span></div>
      <div class="details">
        <h1 class="details__name">Marisol Vance</h1>
        <p class="details__role">Brand Manager</p>
        <p class="details__company">Brindle Capital, Ltd</p>
        <p class="details__address">48 Elm Row, Suite 5<br>Dalton, MA 01226</p>
        <div class="contact">
          <p><span class="contact__label">Phone :</span> +58 412 30 18</p>
          <p><span class="contact__label">Cell :</span> +58 412 30 18</p>
          <p><span class="contact__label">Email :</span> hello@brindlecapital.com</p>
          <p>www.brindlecapital.com</p>
        </div>
      </div>
    </section>

    <section class="card card--back" role="img" aria-label="Card back: navy field with a faint repeating brand pattern and the Brindle Capital name">
      <div class="wordmark"><span class="wordmark__dot"></span><span>Brindle Capital</span></div>
    </section>
  </main>
</body>
</html>
```